Teachers workshop flyer

I need a flyer to inform schools of a workshop for teachers that empowers the teacher to help traumatised and disadvantaged students to engage in successful learning.

I am a teacher and educator and my info for the flyer is attached.

Target Market(s)

Principals and vice-principals who have stressed staff and students and they want things to be better in the school!

Industry/Entity Type

Teacher

```html
<!DOCTYPE html>
<html lang="en">
<head>
<meta charset="utf-8">
<title>Brain-Based Strategies for Student Success</title>
<link rel="stylesheet" href="https://fonts.googleapis.com/css2?family=Roboto+Condensed:wght@700&family=Arimo:ital,wght@0,400;0,700;1,400;1,700&display=swap">
<style>
  :root {
    --sky-light: #e6ded0;
    --sky-mid: #c9bfae;
    --sky-dark: #8f8a80;
    --sky-blue: #7d8ea0;
    --panel: rgba(82, 82, 84, 0.9);
    --title: #ffffff;
    --panel-text: #e4e4e4;
    --rule: #9a9a9a;
    --ink: #111111;
  }
  * { margin: 0; padding: 0; box-sizing: border-box; }
  html, body { width: 1200px; height: 848px; overflow: hidden; background: #fff; }
  .flyer {
    position: relative;
    width: 1200px;
    height: 848px;
    overflow: hidden;
    font-family: "Arimo", Arial, sans-serif;
  }
  .sky-photo {
    position: absolute; inset: 0;
    background:
      radial-gradient(ellipse 420px 260px at 900px 230px, rgba(240,232,218,0.9), transparent 70%),
      radial-gradient(ellipse 500px 300px at 1150px 380px, rgba(125,142,160,0.55), transparent 70%),
      radial-gradient(ellipse 600px 400px at 700px 700px, rgba(236,228,214,0.8), transparent 70%),
      linear-gradient(160deg, var(--sky-dark) 0%, var(--sky-mid) 35%, var(--sky-light) 60%, var(--sky-mid) 100%);
  }
  .side-panel {
    position: absolute;
    left: 32px; top: 0;
    width: 501px; height: 848px;
    background: var(--panel);
  }
  .headline {
    position: absolute;
    left: 32px; top: 44px;
    width: 501px;
    text-align: center;
    font-family: "Roboto Condensed", "Arial Narrow", sans-serif;
    font-weight: 700;
    color: var(--title);
    text-transform: uppercase;
    line-height: 0.94;
    text-shadow: 2px 2px 4px rgba(0,0,0,0.35);
  }
  .headline .line { display: block; font-size: 83px; letter-spacing: 0.5px; }
  .headline .line-big { font-size: 116px; line-height: 0.95; margin-top: 2px; }
  .rule {
    position: absolute;
    height: 1px;
    background: var(--rule);
  }
  .rule::before, .rule::after {
    content: ""; position: absolute; top: -2px;
    width: 5px; height: 5px; border-radius: 50%; background: var(--rule);
  }
  .rule::before { left: -2px; }
  .rule::after { right: -2px; }
  .rule-left { left: 57px; top: 424px; width: 453px; }
  .rule-right-top { left: 565px; top: 424px; width: 600px; }
  .rule-right-bottom { left: 565px; top: 722px; width: 600px; }
  .intro {
    position: absolute;
    left: 72px; top: 458px;
    width: 422px;
    text-align: center;
    color: var(--panel-text);
    font-size: 18px;
    line-height: 24.5px;
  }
  .intro p + p { margin-top: 24px; }
  .details {
    position: absolute;
    left: 574px; top: 437px;
    width: 590px;
    color: var(--ink);
    font-size: 13px;
    line-height: 16.6px;
  }
  .details h2 { font-size: 13px; font-weight: 700; }
  .details .block + .block { margin-top: 16px; }
  .details .quote { font-style: italic; }
  .details ul { list-style: none; font-style: italic; }
  .details li::before { content: "\2022\00a0"; font-style: normal; }
  .contact {
    position: absolute;
    left: 565px; top: 734px;
    width: 600px;
    text-align: center;
    color: var(--ink);
  }
  .contact .phone { font-size: 27px; font-weight: 700; line-height: 36px; }
  .contact .invite { font-size: 18px; line-height: 28px; margin-top: 2px; }
  .contact .web { font-size: 20px; font-weight: 700; line-height: 28px; }
</style>
</head>
<body>
<main class="flyer">
  <div class="sky-photo" role="img" aria-label="Photograph of a seagull soaring with outstretched wings across a cloudy beige and grey sky"></div>

  <div class="side-panel"></div>

  <h1 class="headline">
    <span class="line">Brain-Based</span>
    <span class="line">Strategies</span>
    <span class="line">For Student</span>
    <span class="line line-big">Success</span>
  </h1>

  <div class="rule rule-left"></div>

  <section class="intro">
    <p>Contemporary teaching is a highly complex role as increasing numbers of students attend school without the essential ‘self-skills’ to be truly ‘school-ready’ and successful. Instead these students often seek-out attention in ways that can disruptive in the classroom causing stress and frustration for teachers.</p>
    <p>Dan shows how and why the most effective strategies for these students are guided by a sound understanding of child-development and brain-development - especially where trauma has left lasting impacts. Teachers can learn how to build a student’s self-skills, without the teacher having to become a therapist!</p>
  </section>

  <div class="rule rule-right-top"></div>

  <section class="details">
    <div class="block">
      <h2>About the Presenter:</h2>
      <p><strong><em>Daniel Ashcroft</em></strong> is a Melbourne-based therapist and educator with over twenty years experience working with adults and young people in the area of trauma and recovery. Dan’s seminars are engaging and practical since teachers need effective strategies that will immediately translate into classroom practice. Dan has trained here and overseas in the most effective behavior change strategies.</p>
    </div>
    <div class="block">
      <h2>Teacher Feedback:</h2>
      <p class="quote">“Dan was such an engaging and energetic presenter whom I enjoyed immensely.<br>His presentation on the brain and take away strategies were so practical and meaningful.<br>It was an invaluable session.”</p>
    </div>
    <div class="block">
      <p class="quote">“<strong>My Light-bulb moments:</strong></p>
      <ul>
        <li>I need to CONNECT – not correct – far more often.</li>
        <li>Seeing negative self-talk for what it is.</li>
        <li>Using far more ‘diversions’ in the avoidance loop.”</li>
      </ul>
    </div>
  </section>

  <div class="rule rule-right-bottom"></div>

  <section class="contact">
    <p class="phone">Call - 0400 318 562</p>
    <p class="invite">for more information or to book Dan to come to your school visit</p>
    <p class="web">www.danielashcroft.com.au/studentsuccess</p>
  </section>
</main>
</body>
</html>
```